Business Card Design

I need a business card for a new company based in Australia called "ClinoPath".

Its a cloud program for GPs that allows them to search for the specialist they require using a simple user friendly tool.

I would like the colours to match those in the program (the colours in the logo attached).

The final design should reflect the programs clarity, ease of use and professionalism.

Target Market(s)

GPs and other Health Professionals

Industry/Entity Type

Business

Contact Information for Business Card

ClinoPath; The Whole Consultant Index; Maren Tolhurst CEO; 0417385261; maren@clinopath.example; www.clinopath.example

Requirements
Must have
• Must have the logo attached; the web address and my name and phone number
Nice to have
• the slogan "The Whole Consultant Index"

```html
<!DOCTYPE html>
<html lang="en">
<head>
<meta charset="utf-8">
<title>ClinoPath – Business Card</title>
<link rel="stylesheet" href="https://fonts.googleapis.com/css2?family=Open+Sans:wght@300;400;600&display=swap">
<style>
  :root {
    --page-bg: #d9dadc;
    --brand-blue: #1ba8e0;
    --sky-light: #74c9ee;
    --sky-deep: #4db6e5;
    --ink-grey: #6d7378;
    --card-white: #fbfbfb;
    --tint: #e3f1f9;
    --icon-pointer: #8a9096;
  }
  * { margin: 0; padding: 0; box-sizing: border-box; }
  html, body { width: 1200px; height: 900px; overflow: hidden; }
  body {
    background: var(--page-bg);
    font-family: "Open Sans", Arial, sans-serif;
    position: relative;
  }
  .card {
    position: absolute;
    left: 270px;
    width: 660px;
    height: 377px;
    overflow: hidden;
    box-shadow: 0 6px 18px rgba(0,0,0,0.18);
  }
  .card__backdrop { position: absolute; inset: 0; }

  /* Front */
  .card--front { top: 48px; color: #fff; }
  .card--front .card__backdrop {
    background: linear-gradient(160deg, var(--sky-light), var(--sky-deep));
  }
  .front__brand {
    position: absolute;
    left: 0; right: 0; top: 120px;
    text-align: center;
  }
  .front__name { font-size: 64px; font-weight: 400; letter-spacing: -1px; line-height: 1; }
  .front__tagline { font-size: 19px; font-weight: 300; margin-top: 4px; letter-spacing: 0.3px; }
  .front__rule {
    width: 300px; height: 1px; margin: 20px auto 12px;
    background: rgba(255,255,255,0.7);
  }
  .front__web { font-size: 11px; letter-spacing: 5px; font-weight: 400; }

  /* Back */
  .card--back { top: 475px; }
  .card--back .card__backdrop {
    background: linear-gradient(150deg, var(--card-white) 35%, var(--tint));
  }
  .back__brand { position: absolute; left: 70px; top: 112px; }
  .back__name { font-size: 46px; color: var(--brand-blue); font-weight: 400; letter-spacing: -1px; line-height: 1; }
  .back__tagline { font-size: 14px; color: var(--ink-grey); font-weight: 400; margin-top: 1px; }

  .person { position: absolute; left: 0; top: 210px; display: flex; align-items: center; }
  .person__band {
    background: var(--brand-blue);
    color: #fff;
    width: 255px; height: 30px;
    padding-right: 10px;
    font-size: 18px;
    letter-spacing: 0.5px;
    display: flex; align-items: center; justify-content: flex-end;
  }
  .person__arrow {
    width: 0; height: 0;
    border-top: 6px solid transparent; border-bottom: 6px solid transparent;
    border-left: 8px solid var(--icon-pointer);
    margin: 0 4px;
  }
  .person__role { font-size: 14px; color: var(--ink-grey); }

  .contact { position: absolute; display: flex; flex-direction: column; align-items: flex-start; }
  .contact__icon { width: 22px; height: 26px; margin-bottom: 4px; }
  .contact__text { font-size: 15px; color: var(--ink-grey); letter-spacing: 0.3px; white-space: nowrap; }
  .contact--phone { left: 62px; top: 284px; }
  .contact--phone .contact__icon { margin-left: 8px; }
  .contact--email { left: 270px; top: 236px; }
  .contact--email .contact__icon { margin-left: 50px; }
  .contact--web { left: 430px; top: 190px; }
  .contact--web .contact__icon { margin-left: 40px; }
</style>
</head>
<body>

<section class="card card--front" aria-label="Card front">
  <div class="card__backdrop" role="img" aria-label="Soft blue background where translucent arcs and triangles belong"></div>
  <div class="front__brand">
    <div class="front__name">ClinoPath</div>
    <div class="front__tagline">The Whole Consultant Index</div>
    <div class="front__rule"></div>
    <div class="front__web">www.clinopath.example</div>
  </div>
</section>

<section class="card card--back" aria-label="Card back">
  <div class="card__backdrop" role="img" aria-label="Pale white-to-blue background where faint arcs and triangles belong"></div>

  <div class="back__brand">
    <div class="back__name">ClinoPath</div>
    <div class="back__tagline">The Whole Consultant Index</div>
  </div>

  <div class="person">
    <div class="person__band">MAREN TOLHURST</div>
    <span class="person__arrow"></span>
    <span class="person__role">CEO</span>
  </div>

  <div class="contact contact--web">
    <svg class="contact__icon" viewBox="0 0 22 26" aria-hidden="true">
      <rect width="20" height="20" fill="var(--brand-blue)"/>
      <circle cx="10" cy="10" r="5.5" fill="none" stroke="#fff" stroke-width="1.5"/>
      <path d="M4.5,10 H15.5 M10,4.5 C7,8 7,12 10,15.5 M10,4.5 C13,8 13,12 10,15.5" stroke="#fff" stroke-width="1" fill="none"/>
      <polygon points="6,21 14,21 10,26" fill="var(--icon-pointer)"/>
    </svg>
    <span class="contact__text">www.clinopath.example</span>
  </div>

  <div class="contact contact--email">
    <svg class="contact__icon" viewBox="0 0 22 26" aria-hidden="true">
      <rect width="20" height="20" fill="var(--brand-blue)"/>
      <rect x="4.5" y="6" width="11" height="8" fill="none" stroke="#fff" stroke-width="1.3"/>
      <path d="M4.5,6 L10,11 L15.5,6" fill="none" stroke="#fff" stroke-width="1.3"/>
      <polygon points="6,21 14,21 10,26" fill="var(--icon-pointer)"/>
    </svg>
    <span class="contact__text">maren@clinopath.example</span>
  </div>

  <div class="contact contact--phone">
    <svg class="contact__icon" viewBox="0 0 22 26" aria-hidden="true">
      <rect width="20" height="20" fill="var(--brand-blue)"/>
      <path d="M7,5 L9,5 L10,8 L8.6,9 C9.3,10.6 10.4,11.7 12,12.4 L13,11 L16,12 L16,14 C16,15 15,15.5 14,15.3 C9.5,14.5 6.5,11.5 5.7,7 C5.5,6 6,5 7,5 Z" fill="#fff"/>
      <polygon points="6,21 14,21 10,26" fill="var(--icon-pointer)"/>
    </svg>
    <span class="contact__text">0417385261</span>
  </div>
</section>

</body>
</html>
```